Brightvale Fire Solutions business card, logo and web design.

We need business cards for our new company. We are based in South Africa. We specialise in fire detection, fire prevention, security, access control and CCTV in buildings. We service and install sprinkler systems, fire hose reals and fire extinguishers in buildings. Our slogan in the company is "Compliance is our business" . We strive to be innovators in our field and deliver the best service possible at the best quality. We want to be the best in our field. We don't have any colour preferences as long as it relates to our type of business.
Our target market is clients that owns big buildings with multiple levels, such a malls,office buildings or warehouses.

Target Market(s)

Industry/Entity Type

Fire Safety

Contact Information for Business Card

The front of the card should have the company name (Brightvale Fire Solutions (PTY) LTD. and a description of the company. Fire engineering & security services.

Logo Text

Compliance is our business

Number of Pages Required

4 page

Font styles to use
Serif

Colors

Designer to choose colors to be used in the design.

Requirements
Must have
• The company name, the logo and all the details on the back of the card. It should be simple and not to busy.
Nice to have
• Just something different and new. Brightvale means - innovate so the card should represent our name.
Should not have
• Small pictures or lots of graphics on.

```html
<!DOCTYPE html>
<html lang="en">
<head>
<meta charset="utf-8">
<title>Brightvale Fire Solutions – Business Card</title>
<link rel="stylesheet" href="https://fonts.googleapis.com/css2?family=Tinos:wght@400;700&display=swap">
<style>
  :root {
    --page-bg: #e4e4e4;
    --card-bg: #ffffff;
    --brand-red: #e8174a;
    --deep-red: #b00000;
    --ink: #111111;
    --on-red: #ffffff;
  }
  * { box-sizing: border-box; margin: 0; padding: 0; }
  html, body { width: 1200px; height: 1200px; overflow: hidden; }
  body {
    background: var(--page-bg);
    position: relative;
    font-family: "Tinos", "Times New Roman", serif;
  }
  .card {
    position: absolute;
    width: 480px;
    height: 274px;
    background: var(--card-bg);
  }
  .card--front { left: 359px; top: 270px; }
  .card--back  { left: 362px; top: 628px; }

  .brand { position: absolute; display: flex; align-items: center; gap: 10px; }
  .brand__dot { width: 34px; height: 34px; border-radius: 50%; background: var(--brand-red); flex: none; }
  .brand__name {
    color: var(--brand-red);
    font-weight: 700;
    line-height: 1.1;
    text-transform: uppercase;
  }
  .brand__tagline {
    color: var(--ink);
    text-transform: uppercase;
    letter-spacing: 0.02em;
  }

  .card--front .brand { left: 120px; top: 106px; }
  .card--front .brand__name { font-size: 19px; }
  .card--front .brand__tagline { font-size: 8px; margin-top: 5px; }

  .card--back .brand { left: 34px; top: 28px; gap: 8px; }
  .card--back .brand__dot { width: 28px; height: 28px; }
  .card--back .brand__name { font-size: 15px; }
  .card--back .brand__tagline { font-size: 6.5px; margin-top: 4px; }

  .person {
    position: absolute; left: 306px; top: 52px;
    font-size: 17px; color: var(--deep-red);
  }
  .slogan {
    position: absolute; left: 0; right: 0; top: 114px;
    text-align: center;
    font-size: 16px; font-weight: 700;
    letter-spacing: 0.06em;
    color: var(--deep-red);
  }
  .contact-band {
    position: absolute; left: 0; right: 0; top: 172px; height: 86px;
    background: var(--deep-red);
    color: var(--on-red);
    font-size: 10px;
  }
  .contact-row { position: absolute; white-space: nowrap; }
  .contact-row .label { display: inline-block; }
  .col-left .label { width: 34px; }
  .col-left { left: 42px; }
  .col-right { left: 304px; }
</style>
</head>
<body>

  <section class="card card--front" aria-label="Card front">
    <div class="brand">
      <span class="brand__dot"></span>
      <div>
        <div class="brand__name">Brightvale Fire Solutions<br>(PTY) LTD</div>
        <div class="brand__tagline">Fire engineering &amp; security services</div>
      </div>
    </div>
  </section>

  <section class="card card--back" aria-label="Card back">
    <div class="brand">
      <span class="brand__dot"></span>
      <div>
        <div class="brand__name">Brightvale Fire Solutions<br>(PTY) LTD</div>
        <div class="brand__tagline">Fire engineering &amp; security services</div>
      </div>
    </div>

    <p class="person">Name of the Person</p>
    <p class="slogan">COMPLIANCE IS OUR BUSINESS</p>

    <div class="contact-band">
      <p class="contact-row col-left" style="top:11px"><span class="label">Add :</span>18 Kestrel Avenue.</p>
      <p class="contact-row col-left" style="top:28px"><span class="label"></span>Silverdale. Pretoria. 0042</p>
      <p class="contact-row col-left" style="top:47px"><span class="label">Tel :</span>123-456-789</p>
      <p class="contact-row col-left" style="top:64px"><span class="label">Cel :</span>123-456-789</p>

      <p class="contact-row col-right" style="top:11px">Fax : &nbsp;000-000-00</p>
      <p class="contact-row col-right" style="top:28px">Vat : &nbsp;4812037765</p>
      <p class="contact-row col-right" style="top:47px">Reg : &nbsp;21/048372/07</p>
      <p class="contact-row col-right" style="top:66px">Email : info@brightvalefire.co.za</p>
    </div>
  </section>

</body>
</html>
```